Flier needed for parenting seminar

Hello! We need a 4 by 6 clubcard needed for an upcoming parenting seminar. Flier should be in color, good quality images, and be front/back.
We are looking for something fresh, eye-catching, and not generic. Thanks!
CLUBCARD FRONT:
Veltran Institute presents:
Hearthbound Parenting:
Growing Steadfast Homes
By Shaykh Idris Kamal Tarbusi
Sat & Sun
Oct 22 & 23, 2016
9am - 7pm
Location: ORB Samira Hall
4187 Marlow Blvd
Santa Clara, CA 95127
Seating is limited. Register now!
Www.VeltranInstitute.com
1-877-Veltra7
CLUBCARD BACK:
There are no guarantees in life as to raising children to be how they should. Indeed, even Noah (as) lost his son while the Pharaoh's wife was able to raise Moses (as). And while traditionally a woman rears the child, Zakariyah (as) was a man chosen to raise one. The variety of scenarios in the Quran cover all possibilities. It is therefore worth reflecting on them to gain insight and draw parenting lessons.
So come and explore the Quranic view and prophetic guidelines for raising children. We hope this course serves as a landmark for you to know best practices and tools available to you, rooted in Quranic wisdom as well as our own experiences.
Some topics:
- The ways of Quranic raising
- Tools & examples from The Book
- What not to do
- Truth vs wisdom
www.VeltranInstitute.com
1-877-Veltra7
Parents, ppl considering becoming parents, ppl studying child development
- Fresh
- Eye-catching, not generic.
- Silhouette of mother/father with a young child.
- Maybe even praying together...

```html
<!DOCTYPE html>
<html lang="en">
<head>
<meta charset="utf-8">
<title>Hearthbound Parenting – Clubcard</title>
<link rel="stylesheet" href="https://fonts.googleapis.com/css2?family=Cabin:ital,wght@0,400;0,500;0,600;1,400&display=swap">
<style>
  :root {
    --page: #ffffff;
    --front-bg: #000000;
    --back-bg: #4b4a1d;
    --frame: #8c8a3c;
    --cream: #e9dfc2;
    --pale: #dcd9a8;
    --ink-light: #f1ecd8;
    --photo-dark: #140f0b;
    --photo-skin: #b98a6c;
  }
  * { margin: 0; padding: 0; box-sizing: border-box; }
  html, body {
    width: 896px; height: 1200px; overflow: hidden;
    background: var(--page);
    font-family: "Cabin", "Trebuchet MS", sans-serif;
  }
  .card {
    position: absolute; left: 29px; width: 806px; height: 547px;
    box-shadow: 0 6px 14px rgba(0,0,0,0.35);
  }
  .card--front { top: 31px; background: var(--front-bg); }
  .card--back { top: 596px; background: var(--back-bg); }
  .frame {
    position: absolute; left: 26px; top: 27px; right: 28px; bottom: 30px;
    border: 2px solid var(--frame);
  }
  .abs { position: absolute; }

  /* Front */
  .presenter {
    left: 0; right: 0; top: 52px; text-align: center;
    font-style: italic; font-size: 14px; color: var(--pale);
  }
  .front-title {
    left: 0; right: 0; top: 90px; text-align: center;
    font-size: 27px; font-weight: 400; color: var(--pale); letter-spacing: -0.3px;
  }
  .front-speaker {
    left: 0; right: 0; top: 134px; text-align: center;
    font-size: 18px; font-weight: 500; color: var(--pale);
  }
  .divider { left: 329px; top: 175px; width: 148px; height: 12px; }
  .details { left: 68px; color: var(--cream); line-height: 1; }
  .details--days { top: 211px; font-size: 23px; }
  .details--date { top: 238px; font-size: 23px; }
  .details--time { top: 266px; font-size: 23px; }
  .details--venue { top: 302px; font-size: 21px; }
  .details--address { top: 327px; font-size: 15px; }
  .details--cta { top: 381px; font-size: 19px; }
  .details--web { top: 421px; font-size: 18px; font-weight: 600; font-variant: small-caps; letter-spacing: 0.3px; }
  .details--phone { top: 445px; font-size: 28px; color: var(--ink-light); text-transform: uppercase; }
  .photo-hands {
    left: 437px; top: 257px; width: 342px; height: 261px;
    background: radial-gradient(ellipse at 62% 55%, var(--photo-skin) 0%, #7d5b46 35%, var(--photo-dark) 75%);
  }

  /* Back */
  .back-head { left: 58px; top: 55px; color: var(--ink-light); font-weight: 500; line-height: 23px; }
  .back-head__title { font-size: 19px; font-weight: 600; }
  .back-head__speaker { font-size: 17px; }
  .back-copy {
    left: 58px; top: 122px; width: 700px;
    font-size: 15.5px; line-height: 21px; color: var(--cream);
  }
  .back-copy p + p { margin-top: 15px; }
  .topics { left: 58px; top: 316px; font-size: 15.5px; line-height: 21px; color: var(--cream); list-style: none; }
  .back-cta {
    left: 58px; width: 410px; top: 437px; text-align: center; color: var(--ink-light);
  }
  .back-cta__line { font-size: 18px; font-weight: 600; text-transform: uppercase; letter-spacing: -0.3px; }
  .back-cta__web { margin-top: 10px; font-size: 17px; font-weight: 600; }
  .back-cta__phone { font-size: 17px; font-weight: 600; text-transform: uppercase; }
  .art-family {
    left: 486px; top: 295px; width: 248px; height: 212px; border-radius: 40% 40% 8px 8px;
    background: linear-gradient(100deg, #2b53a8 0%, #3f8fd6 50%, #4aa63a 100%);
  }
</style>
</head>
<body>
  <section class="card card--front">
    <div class="frame"></div>
    <p class="abs presenter">Veltran Institute presents:</p>
    <h1 class="abs front-title">HEARTHBOUND PARENTING: Growing Steadfast Homes</h1>
    <p class="abs front-speaker">by Shaykh Idris Kamal Tarbusi</p>
    <svg class="abs divider" viewBox="0 0 148 12" aria-hidden="true">
      <line x1="0" y1="6" x2="148" y2="6" stroke="#b9b583" stroke-width="1"/>
      <circle cx="74" cy="6" r="2.5" fill="#d9d5a2"/>
    </svg>
    <p class="abs details details--days">Saturday &amp; Sunday</p>
    <p class="abs details details--date">Oct. 22 &amp; 23, 2016</p>
    <p class="abs details details--time">9am - 7pm</p>
    <p class="abs details details--venue">Location: ORB Samira Hall</p>
    <p class="abs details details--address">4187 Marlow Blvd, Santa Clara, CA 95127</p>
    <p class="abs details details--cta">Seating is limited. Register now!</p>
    <p class="abs details details--web">Www.VeltranInstitute.com</p>
    <p class="abs details details--phone">1-877-Veltra7</p>
    <div class="abs photo-hands" role="img" aria-label="Photo of a parent's and a child's hands raised together in prayer, holding prayer beads"></div>
  </section>

  <section class="card card--back">
    <div class="frame"></div>
    <div class="abs back-head">
      <h2 class="back-head__title">HEARTHBOUND PARENTING:&nbsp; Growing Steadfast Homes</h2>
      <p class="back-head__speaker">by Shaykh Idris Kamal Tarbusi</p>
    </div>
    <div class="abs back-copy">
      <p>There are no guarantees in life as to raising children to be how they should. Indeed, even Noah (as) lost his son while the Pharaoh's wife was able to raise Moses (as). And while traditionally a woman rears the child, Zakariyah (as) was a man chosen to raise one. The variety of scenarios in the Quran cover all possibilities. It is therefore worth reflecting on them to gain insight and draw parenting lessons.</p>
      <p>So come and explore the Quranic view and prophetic guidelines for raising children. We hope this course serves as a landmark for you to know best practices and tools available to you, rooted in Quranic wisdom as well as our own experiences.</p>
    </div>
    <ul class="abs topics">
      <li>Some topics:</li>
      <li>- The ways of Quranic raising</li>
      <li>- Tools &amp; examples from The Book</li>
      <li>- What not to do</li>
      <li>- Truth vs wisdom</li>
    </ul>
    <div class="abs back-cta">
      <p class="back-cta__line">Seating is limited. Register now!</p>
      <p class="back-cta__web">www.VeltranInstitute.com</p>
      <p class="back-cta__phone">1-877-Veltra7</p>
    </div>
    <div class="abs art-family" role="img" aria-label="Illustration of a mother in a blue headscarf reading a book with a daughter and a son in a green cap"></div>
  </section>
</body>
</html>
```